Medical Cannabis company is looking for a LOGO design *

SILVER MERIDIAN (SM) is a new company in the Israeli medical cannabis industry. We will engage in PREMIUM medical cannabis growing and cultivation and also manufacturing of HIGH-END cannabis based medical products.
the design should reflect luxury, high-end and Pharma-grade products.
the design should use color GOLD and NOT using the famous cannabis leaf !

Target Market(s)

international medical cannabis Pharmaceutical companies
and of course local and international patients

Contact Information for Business Card

Ron Ben-Amit
Founder and CEO

Silver Meridian
Medical grade cannabis

ronbenamit@mailpost-example.com
972-52-3186407

Colors
ffc214
fbed22

Requirements
Must have
• clean and simple
• luxury
• gold !!
• (can also have green for Cannabis and/or blue for Pharma)
Should not have
• cannabis leaf

```html
<!DOCTYPE html>
<html lang="en">
<head>
<meta charset="utf-8">
<title>Silver Meridian – Business Card</title>
<link href="https://fonts.googleapis.com/css2?family=Cinzel:wght@400;700&family=Lato:wght@400;700&display=swap" rel="stylesheet">
<style>
  :root {
    --page-bg: #ecebe8;
    --card-dark-top: #2c2c2c;
    --card-dark-bottom: #1c1c1c;
    --card-light: #ffffff;
    --gold: #ffc214;
    --gold-light: #fbed22;
    --silver-grey: #b9b9b9;
    --ink: #111111;
    --card-shadow: rgba(0, 0, 0, 0.18);
  }
  * { margin: 0; padding: 0; box-sizing: border-box; }
  html, body {
    width: 1200px;
    height: 900px;
    overflow: hidden;
    background: var(--page-bg);
  }
  .canvas {
    width: 1200px;
    height: 900px;
    display: flex;
    flex-direction: column;
    align-items: center;
    justify-content: center;
    gap: 56px;
  }
  .card {
    width: 600px;
    height: 343px;
    box-shadow: 0 6px 18px var(--card-shadow);
    position: relative;
  }
  .card--front {
    background: linear-gradient(160deg, var(--card-dark-top), var(--card-dark-bottom));
    display: flex;
    flex-direction: column;
    align-items: center;
    justify-content: center;
  }
  .brand {
    display: flex;
    align-items: center;
    gap: 14px;
  }
  .brand__dot {
    width: 18px;
    height: 18px;
    border-radius: 50%;
    background: var(--gold);
  }
  .brand__name {
    font-family: "Lato", sans-serif;
    font-weight: 700;
    font-size: 44px;
    color: var(--gold);
    letter-spacing: 0.5px;
  }
  .brand__tagline {
    margin-top: 6px;
    font-family: "Cinzel", serif;
    font-weight: 400;
    font-size: 19px;
    letter-spacing: 5px;
    color: var(--silver-grey);
    text-transform: uppercase;
  }
  .card--back {
    background: var(--card-light);
  }
  .contact {
    position: absolute;
    left: 250px;
    top: 92px;
    color: var(--ink);
  }
  .contact__name {
    font-family: "Cinzel", serif;
    font-weight: 700;
    font-size: 21px;
    letter-spacing: 1px;
    text-transform: uppercase;
  }
  .contact__role {
    font-family: "Lato", sans-serif;
    font-size: 14px;
    letter-spacing: 0.5px;
    text-transform: uppercase;
    margin-top: 2px;
  }
  .contact__rule {
    width: 220px;
    height: 1px;
    background: var(--ink);
    margin: 16px 0 14px -20px;
  }
  .contact__line {
    font-family: "Lato", sans-serif;
    font-size: 15px;
    letter-spacing: 0.5px;
    text-transform: uppercase;
    line-height: 1.45;
  }
</style>
</head>
<body>
  <main class="canvas">
    <section class="card card--front" aria-label="Business card front">
      <div class="brand">
        <span class="brand__dot"></span>
        <span class="brand__name">Silver Meridian</span>
      </div>
      <p class="brand__tagline">Medical Grade Cannabis</p>
    </section>

    <section class="card card--back" aria-label="Business card back">
      <div class="contact">
        <h1 class="contact__name">Ron Ben-Amit</h1>
        <p class="contact__role">Founder and CEO</p>
        <div class="contact__rule"></div>
        <p class="contact__line">972-52-3186407</p>
        <p class="contact__line">ronbenamit@mailpost-example.com</p>
      </div>
    </section>
  </main>
</body>
</html>
```